Business Card Design

i am looking a business card for a car rental company long with Taxi service also a logo.

what is the latest with my project

Industry/Entity Type

Business

Contact Information for Business Card

name of the Company is Kestrel Bay Motor Leasing and Taxi Services
Address: Harrow Point Village, St. Linden Parish
Tele# 555-0142/5550187-555-0163
Email: lorimbeck@quillmarsh.test

Font styles to use
Script

```html
<!DOCTYPE html>
<html lang="en">
<head>
<meta charset="utf-8">
<title>Kestrel Bay Motor Leasing — Business Card Options</title>
<link href="https://fonts.googleapis.com/css2?family=Arimo:wght@400&family=Montserrat:wght@800&display=swap" rel="stylesheet">
<style>
  :root {
    --page: #ffffff;
    --ink: #1f1f1f;
    --red: #e3262c;
    --yellow: #f5e21a;
    --black: #0a0a0a;
    --paper: #fdfdfd;
    --silver-light: #f7f7f7;
    --silver-dark: #9a9a9a;
  }
  * { box-sizing: border-box; margin: 0; padding: 0; }
  html, body { width: 719px; height: 1200px; overflow: hidden; background: var(--page); }
  .sheet { position: relative; width: 719px; height: 1200px; }

  .option-number {
    position: absolute; left: 26px;
    font: 400 28px/1 "Arimo", sans-serif; color: var(--ink);
  }

  .card {
    position: absolute; width: 566px; height: 343px;
    border-radius: 34px; overflow: hidden;
    background: var(--paper);
    box-shadow: 0 4px 14px rgba(0,0,0,.35);
  }
  .card-art { position: absolute; inset: 0; width: 100%; height: 100%; }

  .brand-name {
    position: absolute; left: 90px; top: 52px; width: 400px;
    font: 800 25px/1.15 "Montserrat", sans-serif;
    text-transform: uppercase; text-align: center;
  }
  .card--silver .brand-name, .card--white .brand-name { color: var(--red); }
  .card--night .brand-name { color: var(--yellow); }

  .contact {
    position: absolute; left: 76px; top: 222px;
    list-style: none; display: flex; flex-direction: column; gap: 9px;
    font-family: "Arimo", sans-serif; font-size: 18px; color: var(--ink);
  }
  .contact li { display: flex; align-items: center; gap: 8px; height: 20px; }
  .contact .icon { width: 14px; height: 14px; flex: none; fill: currentColor; }
  .contact .phone { font: 800 18px "Montserrat", sans-serif; letter-spacing: .2px; }
  .card--silver .icon, .card--white .icon { color: var(--red); }
  .card--white .contact { color: #ffffff; }
  .card--night .icon { color: var(--black); }
</style>
</head>
<body>
<main class="sheet">

  <span class="option-number" style="top:176px">1</span>
  <section class="card card--silver" style="left:86px; top:43px">
    <svg class="card-art" viewBox="0 0 590 357" preserveAspectRatio="none" aria-hidden="true">
      <defs>
        <radialGradient id="silver" cx="0.45" cy="0.35" r="0.7">
          <stop offset="0" stop-color="var(--silver-light)"/>
          <stop offset="1" stop-color="var(--silver-dark)"/>
        </radialGradient>
      </defs>
      <path d="M0 0H590V150H310L180 183H0Z" fill="url(#silver)"/>
      <polyline points="0,186 180,186 310,154 590,154" fill="none" stroke="var(--red)" stroke-width="5"/>
      <polyline points="0,193 180,193 310,161 590,161" fill="none" stroke="var(--black)" stroke-width="5"/>
    </svg>
    <p class="brand-name">Kestrel Bay Motor Leasing<br>&amp; Taxi Services</p>
    <ul class="contact">
      <li><svg class="icon" viewBox="0 0 14 14"><path d="M7 1 0 6h2v7h10V6h2zM5 8h4v5H5z"/></svg>Harrow Point Village, St. Linden Parish</li>
      <li class="phone"><svg class="icon" viewBox="0 0 14 14"><path d="M3 1l3 3-2 2c1 2 2 3 4 4l2-2 3 3-2 2C5 13 1 9 1 3z"/></svg>555-0142/ 5550187-555-0163</li>
      <li><svg class="icon" viewBox="0 0 14 14"><path d="M1 3h12v9H1zM2 4l5 4 5-4v-.1H2zM2 5v6h10V5L7 9z" fill-rule="evenodd"/></svg>lorimbeck@quillmarsh.test</li>
    </ul>
  </section>

  <span class="option-number" style="top:574px">2</span>
  <section class="card card--white" style="left:93px; top:434px">
    <svg class="card-art" viewBox="0 0 590 357" preserveAspectRatio="none" aria-hidden="true">
      <path d="M0 197H180L310 165H590V357H0Z" fill="var(--black)"/>
      <polyline points="0,182 180,182 310,150 590,150" fill="none" stroke="var(--black)" stroke-width="4"/>
      <polyline points="0,190 180,190 310,158 590,158" fill="none" stroke="var(--red)" stroke-width="5"/>
    </svg>
    <p class="brand-name">Kestrel Bay Motor Leasing<br>&amp; Taxi Services</p>
    <ul class="contact">
      <li><svg class="icon" viewBox="0 0 14 14"><path d="M7 1 0 6h2v7h10V6h2zM5 8h4v5H5z"/></svg>Harrow Point Village, St. Linden Parish</li>
      <li class="phone"><svg class="icon" viewBox="0 0 14 14"><path d="M3 1l3 3-2 2c1 2 2 3 4 4l2-2 3 3-2 2C5 13 1 9 1 3z"/></svg>555-0142/ 5550187-555-0163</li>
      <li><svg class="icon" viewBox="0 0 14 14"><path d="M1 3h12v9H1zM2 4l5 4 5-4v-.1H2zM2 5v6h10V5L7 9z" fill-rule="evenodd"/></svg>lorimbeck@quillmarsh.test</li>
    </ul>
  </section>

  <span class="option-number" style="top:974px">3</span>
  <section class="card card--night" style="left:101px; top:823px">
    <svg class="card-art" viewBox="0 0 590 357" preserveAspectRatio="none" aria-hidden="true">
      <path d="M0 0H590V147H310L180 180H0Z" fill="var(--black)"/>
      <polyline points="0,183 180,183 310,151 590,151" fill="none" stroke="var(--yellow)" stroke-width="5"/>
      <polyline points="0,190 180,190 310,158 590,158" fill="none" stroke="#2a2a2a" stroke-width="5"/>
    </svg>
    <p class="brand-name">Kestrel Bay Motor Leasing<br>&amp; Taxi Services</p>
    <ul class="contact">
      <li><svg class="icon" viewBox="0 0 14 14"><path d="M7 1 0 6h2v7h10V6h2zM5 8h4v5H5z"/></svg>Harrow Point Village, St. Linden Parish</li>
      <li class="phone"><svg class="icon" viewBox="0 0 14 14"><path d="M3 1l3 3-2 2c1 2 2 3 4 4l2-2 3 3-2 2C5 13 1 9 1 3z"/></svg>555-0142/ 5550187-555-0163</li>
      <li><svg class="icon" viewBox="0 0 14 14"><path d="M1 3h12v9H1zM2 4l5 4 5-4v-.1H2zM2 5v6h10V5L7 9z" fill-rule="evenodd"/></svg>lorimbeck@quillmarsh.test</li>
    </ul>
  </section>

</main>
</body>
</html>
```